Young, dynamic furniture company requires leaflet design

We require a new leaflet for our modern furniture company which supplies furniture and appliances to the property and development market.
Bramblecourt Furniture has become one of the leading furniture & appliance suppliers to the property market withing London. With over 10 years experience, we have increased our business to supply not only Private Landlords and Managing Agents, but also Property Developers, Housing Associations and Local Councils.
We offer not only a complete range of furniture which includes beds, wardrobes, dining sets and sofas, but also a high quality, full delivery and assembly service to help you with all our furnishing needs.

Target Market(s)

Private Landlords, Developers, Letting & Managing Agents

Industry/Entity Type

Furniture Store

Font styles to use
Sans Serif

Colors
0255a3
3176b5
85abd2
cfdeed
eaf1f7

Requirements
Must have
• Contact details,
• Our services:
• FREE next day delivery within the M25
• Free furniture assembly
• Free key pick up & drop off
• Free furniture removal (on a like-for-like basis)
• All types of furniture supplied - from basic to luxury

```html
<!DOCTYPE html>
<html lang="en">
<head>
<meta charset="utf-8">
<title>Bramblecourt Furniture Leaflet</title>
<link rel="stylesheet" href="https://fonts.googleapis.com/css2?family=Roboto:wght@300;400&display=swap">
<style>
  :root {
    --backdrop: #111111;
    --paper: #f6f6f6;
    --navy-panel: #22376c;
    --navy-band: #1f3a73;
    --ink-navy: #232a57;
    --ink-grey: #8a8a8a;
    --ink-body: #666666;
    --brand-blue: #1670b9;
    --bar-sofas: #0a56a8;
    --bar-beds: #242a5c;
    --bar-bedroom: #7d90c9;
    --bar-dining: #1776c0;
    --bar-appliances: #8d969d;
    --bar-packages: #5a1d52;
    --badge-navy: #252a57;
    --badge-lilac: #6f86c7;
    --badge-plum: #5b1e54;
    --badge-blue: #1572be;
    --white: #ffffff;
  }
  * { margin: 0; padding: 0; box-sizing: border-box; }
  html, body {
    width: 1189px; height: 1200px; overflow: hidden;
    background: var(--backdrop);
    font-family: 'Roboto', sans-serif;
  }
  .leaflet {
    position: absolute; left: 182px; top: 20px;
    width: 825px; height: 1160px;
    background: var(--paper); overflow: hidden;
  }
  .hero-photo { position: absolute; left: 0; top: 0; width: 825px; height: 800px; }
  .brand-panel { position: absolute; left: 0; top: 0; width: 825px; height: 660px; }
  .brand-name {
    position: absolute; left: 34px; width: 297px; top: 150px;
    text-align: center; color: var(--white);
    font-weight: 300; font-size: 20px;
  }
  .brand-tagline {
    position: absolute; left: 34px; width: 297px; top: 180px;
    text-align: center; color: var(--white);
    font-weight: 300; font-size: 11px;
  }
  .brand-mark {
    position: absolute; left: 162px; top: 70px;
    width: 40px; height: 40px; background: var(--brand-blue);
  }
  .range-list { position: absolute; left: 74px; top: 0; width: 257px; list-style: none; }
  .range-list li {
    position: absolute; left: 0; width: 257px; height: 35px;
    color: var(--white); font-weight: 400; font-size: 20px;
    text-align: right; padding-right: 12px; line-height: 35px;
    box-shadow: -2px 2px 3px rgba(0,0,0,0.35);
  }
  .bar-sofas { top: 210px; background: var(--bar-sofas); }
  .bar-beds { top: 256px; background: var(--bar-beds); }
  .bar-bedroom { top: 300px; background: var(--bar-bedroom); }
  .bar-dining { top: 345px; background: var(--bar-dining); }
  .bar-appliances { top: 391px; background: var(--bar-appliances); }
  .bar-packages { top: 437px; background: var(--bar-packages); }
  .service-badge {
    position: absolute; width: 112px; height: 112px; border-radius: 50%;
    color: var(--white); text-align: center;
    display: flex; flex-direction: column; justify-content: center;
    box-shadow: 0 2px 4px rgba(0,0,0,0.45);
    font-weight: 300; font-size: 12px; line-height: 15px;
  }
  .service-badge strong { font-weight: 400; font-size: 17px; line-height: 19px; }
  .badge-delivery { left: 220px; top: 531px; background: var(--badge-navy); }
  .badge-assembly { left: 377px; top: 565px; background: var(--badge-lilac); }
  .badge-removal { left: 531px; top: 621px; background: var(--badge-plum); }
  .badge-keys { left: 678px; top: 688px; background: var(--badge-blue); }
  .promise-title {
    position: absolute; left: 0; width: 588px; top: 762px;
    text-align: center; color: var(--ink-navy);
    font-weight: 400; font-size: 47px;
  }
  .promise-text {
    position: absolute; left: 0; width: 588px; top: 840px;
    text-align: center; color: var(--ink-grey);
    font-weight: 400; font-size: 27px; line-height: 33px;
  }
  .web-address {
    position: absolute; left: 0; width: 588px; top: 935px;
    text-align: center; color: var(--brand-blue);
    font-weight: 400; font-size: 36px; letter-spacing: 8px;
  }
  .contact { position: absolute; font-weight: 300; font-size: 14px; line-height: 18px; color: var(--ink-body); }
  .contact-label { color: var(--brand-blue); font-weight: 400; font-size: 15px; }
  .showroom { left: 36px; top: 1046px; }
  .showroom .contact-label { margin-bottom: 8px; }
  .phones { left: 320px; top: 1075px; }
  .phones span { color: var(--brand-blue); }
  .opening { right: 30px; top: 1032px; text-align: right; font-size: 16px; line-height: 20px; }
  .opening .contact-label { font-size: 16px; }
  .footer-band { position: absolute; left: 0; top: 1136px; width: 825px; height: 24px; background: var(--navy-band); }
</style>
</head>
<body>
  <main class="leaflet">
    <svg class="hero-photo" viewBox="0 0 825 800" role="img" aria-label="Photo of a bright white bedroom with a made bed, bedside lamp, window with curtains and framed pictures">
      <defs>
        <linearGradient id="roomTone" x1="0" y1="0" x2="1" y2="1">
          <stop offset="0" stop-color="#8f9fb8"/>
          <stop offset="0.5" stop-color="#a9b6c8"/>
          <stop offset="1" stop-color="#8c8580"/>
        </linearGradient>
      </defs>
      <polygon points="0,0 825,0 825,796 0,576" fill="url(#roomTone)"/>
    </svg>

    <svg class="brand-panel" viewBox="0 0 825 660" aria-hidden="true">
      <polygon points="34,0 331,0 331,482 34,646" fill="var(--navy-panel)"/>
    </svg>

    <div class="brand-mark"></div>
    <div class="brand-name">BRAMBLECOURT FURNITURE</div>
    <div class="brand-tagline">TRADE FURNITURE SOLUTIONS</div>

    <ul class="range-list">
      <li class="bar-sofas">SOFAS</li>
      <li class="bar-beds">BEDS</li>
      <li class="bar-bedroom">BEDROOM FURNITURE</li>
      <li class="bar-dining">DINING</li>
      <li class="bar-appliances">APPLIANCES</li>
      <li class="bar-packages">FURNITURE PACKAGES</li>
    </ul>

    <div class="service-badge badge-delivery"><strong>FREE</strong>NEXT DAY<br>DELIVERY</div>
    <div class="service-badge badge-assembly"><strong>FREE</strong>FURNITURE<br>ASSEMBLY</div>
    <div class="service-badge badge-removal"><strong>FREE</strong>FURNITURE<br>REMOVAL</div>
    <div class="service-badge badge-keys"><strong>FREE</strong>KEY PICK UP &amp;<br>DROP OFF</div>

    <h1 class="promise-title">THE BCF PROMISE</h1>
    <p class="promise-text">ALL TYPES OF FURNITURE SUPPLIED<br>FROM BASIC TO LUXURY</p>
    <p class="web-address">www.bramblecourt.co.uk</p>

    <div class="contact showroom">
      <div class="contact-label">Showroom:</div>
      Unit 7 Larkfield Trade Park,<br>Osier Lane, London, N17 4XT
    </div>
    <div class="contact phones">
      <span>T:</span> 020 7946 0321<br><span>F :</span> 020 7946 0322
    </div>
    <div class="contact opening">
      <div class="contact-label">Opening Times:</div>
      Mon - Fri: 9am - 6pm<br>Sat: 10am - 5pm<br>Sun: 11am - 5pm
    </div>

    <div class="footer-band"></div>
  </main>
</body>
</html>
```